Web Design job - Condo Debts Collection Business needs a Web Design

I need a site for a client, who works with condo debts collection, and ensure all revenues provided by condo fees will be always available to the building manager of condo on a specific date, regardless of defaults.
I have the visual identity (logo, slogan and colors) of the company, and some requirements on layout (kind of slider, menu options, phone number on a noble position, etc) - maybe I can do a sketch, but I like the idea of give some freedom to designer.

*** PLEASE, we have no interest in templates. We want something new***

Target Market(s)

I have two targets for this design: - Condominium's building manager. This target is looking for a solution to overdue debts on it's condo. - Residents on condominiums. This target wants to live in a better place, where their neighbors pay their condominium fees on time.

Number of Pages Required

1 page

Requirements
Must have
• - Slider with title, some short text related, a nice image (I prefer happy and/or peaceful family, people doing business, happy friends, and so on).
• - I have a special attention to menu. I'm looking for one I can have a nice effect, more elegant, charming, kind of innovative.
• - Phone number on the top (or clearly visible).
• - Member log in area or icon on the top (or clearly visible).
• - News/articles area.
• - Modern fonts, with good quality, sans-serif on areas where reading is more intensive (prefer Google web-fonts).
• - Colors specified on attached files.
Nice to have
• - Clear background color, cause it's better to read larger texts (like articles). Dark backgrounds makes reading difficult.
• - A site with effects (like shadows, lines, curves, gradients, lights) is usually pretty.
• - I pay attention on beautiful footers.
Should not have
• - Images with a lot of money (I don't sell richness, I sell tranquility, peace, harmony, safety).
• - Poor menu.

```html
<!DOCTYPE html>
<html lang="en">
<head>
<meta charset="utf-8">
<title>Veralt – Condo Collections</title>
<link rel="stylesheet" href="https://fonts.googleapis.com/css2?family=Open+Sans:wght@400;600;700&display=swap">
<style>
:root{
  --gold:#e3aa26;
  --gold-dark:#c9962f;
  --gold-light:#f0c64a;
  --ink:#231f20;
  --text:#333;
  --page:#f6f6f6;
  --white:#fff;
  --rule:#cfcfcf;
  --hero-a:#5d6b4a;
  --hero-b:#2e3a2a;
}
*{margin:0;padding:0;box-sizing:border-box}
html,body{width:735px;height:1200px;overflow:hidden}
body{position:relative;background:var(--page);font-family:"Open Sans",Arial,sans-serif;color:var(--text)}
.abs{position:absolute}

/* header */
.brand{left:26px;top:18px;display:flex;align-items:center;gap:10px}
.brand-mark{width:44px;height:44px;background:var(--gold)}
.brand-text{display:flex;flex-direction:column}
.brand-name{font-size:34px;font-weight:700;color:var(--ink);line-height:36px;letter-spacing:-.5px}
.brand-tag{font-size:7px;font-weight:600;color:var(--ink);letter-spacing:.2px}
.phone{left:474px;top:20px;display:flex;align-items:center;gap:8px;font-size:19px;color:var(--ink)}
.login{left:658px;top:20px;width:58px;height:22px;border:2px solid var(--gold);color:var(--gold);font-size:13px;font-weight:600;text-align:center;line-height:18px}

/* hero */
.hero{left:0;top:94px;width:735px;height:380px}
.hero-photo{position:absolute;inset:0;background:radial-gradient(ellipse at 60% 40%,#8d8a76 0%,var(--hero-a) 45%,var(--hero-b) 100%)}
.hero-title{left:0;width:735px;top:186px;text-align:center;color:var(--white);font-size:40px;font-weight:700;letter-spacing:.5px}
.hero-sub{left:0;width:735px;top:236px;text-align:center;color:var(--white);font-size:20px;font-weight:600}
.hero-btn{left:301px;top:289px;width:144px;height:34px;border:1.5px solid var(--white);color:var(--white);font-size:13px;font-weight:600;text-align:center;line-height:31px}
.dots{left:331px;top:355px;display:flex;gap:12px}
.dot{width:14px;height:14px;border-radius:50%;background:#e6e6e6}
.dot.active{background:var(--gold-light)}

/* nav */
.nav-bar{left:138px;top:81px;width:464px;height:32px}
.nav-items{position:absolute;left:138px;top:81px;width:464px;height:32px;font-size:13px;font-weight:600;color:var(--white);line-height:32px}
.nav-items span{position:absolute;top:0;white-space:nowrap}

/* welcome card */
.welcome{left:179px;top:398px;width:372px;height:274px;background:var(--white);box-shadow:0 2px 5px rgba(0,0,0,.18);text-align:center}
.welcome-title{margin-top:54px;font-size:27px;color:var(--ink);font-weight:400}
.welcome-title b{color:var(--gold);font-weight:700;margin-left:8px}
.welcome-rule{margin:10px auto 0;width:268px;height:1px;background:var(--rule);position:relative}
.welcome-rule::after{content:"";position:absolute;left:92px;top:-1px;width:86px;height:2px;background:var(--gold)}
.welcome-copy{margin:10px auto 0;width:320px;font-size:13.5px;line-height:26px}

/* news */
.news-title{left:0;width:735px;top:732px;text-align:center;font-size:28px;font-weight:400;color:var(--ink)}
.news-arrow{top:742px;width:12px;height:20px}
.news-rule{left:113px;top:780px;width:537px;height:1px;background:var(--rule)}
.news-rule::after{content:"";position:absolute;left:178px;top:-1px;width:179px;height:2px;background:var(--gold)}
.post{top:800px;width:164px}
.post-photo{width:160px;height:108px;margin-top:2px}
.post-photo.family{background:linear-gradient(135deg,#4c7b78 0%,#a88d78 55%,#e2dcd6 100%)}
.post-photo.deal{background:linear-gradient(180deg,#b9cde0 0%,#a8a39c 55%,#5a8a3c 100%)}
.post-date{margin-top:12px;font-size:10.5px;color:var(--ink)}
.post-text{margin-top:6px;font-size:10px;line-height:12.5px;color:#444}
.post-btn{margin-top:10px;display:inline-block;background:var(--gold-dark);color:var(--white);font-size:10px;padding:0 6px;height:21px;line-height:21px}

/* footer */
.footer{left:0;top:1012px;width:735px;height:188px;background:var(--ink);color:var(--white)}
.foot-head{top:26px;font-size:12.5px;font-weight:400}
.foot-list{top:61px;font-size:13px;line-height:17px;list-style:none}
.foot-map{left:516px;top:59px;width:122px;height:80px;background:linear-gradient(135deg,#8fb3d9 0%,#d8dadb 35%,#e4e2dc 70%,#bcd3b2 100%)}
.foot-rule{left:0;top:150px;width:735px;height:1px;background:#6b6768}
.foot-rule::after{content:"";position:absolute;left:245px;top:-1px;width:247px;height:2px;background:var(--gold)}
.foot-copy{top:162px;font-size:10px}
</style>
</head>
<body>

<header>
  <div class="abs brand">
    <div class="brand-mark"></div>
    <div class="brand-text">
      <span class="brand-name">Veralt</span>
      <span class="brand-tag">CONDO COLLECTIONS</span>
    </div>
  </div>
  <div class="abs phone">
    <svg width="18" height="18" viewBox="0 0 24 24"><path fill="#e3aa26" d="M6.6 10.8a15.1 15.1 0 0 0 6.6 6.6l2.2-2.2c.3-.3.7-.4 1-.2 1.1.4 2.3.6 3.6.6.6 0 1 .4 1 1V20c0 .6-.4 1-1 1A17 17 0 0 1 3 4c0-.6.4-1 1-1h3.5c.6 0 1 .4 1 1 0 1.3.2 2.5.6 3.6.1.3 0 .7-.2 1z"/></svg>
    <span>(020) 4821 9036</span>
  </div>
  <div class="abs login">LOGIN</div>
</header>

<section class="abs hero">
  <div class="hero-photo" role="img" aria-label="Smiling young man relaxing outdoors among green trees"></div>
</section>
<svg class="abs" style="left:0;top:438px" width="735" height="40" viewBox="0 0 735 40">
  <polygon fill="#f6f6f6" points="0,0 180,32 180,40 0,40"/>
  <polygon fill="#f6f6f6" points="735,0 551,32 551,40 735,40"/>
  <rect fill="#f6f6f6" x="179" y="32" width="373" height="8"/>
</svg>
<h1 class="abs hero-title">WELCOME TO VERALT</h1>
<p class="abs hero-sub">Your number one debt collector</p>
<div class="abs hero-btn">LEARN MORE</div>
<div class="abs dots"><span class="dot active"></span><span class="dot"></span><span class="dot"></span></div>

<nav>
  <svg class="abs nav-bar" viewBox="0 0 464 32">
    <defs>
      <linearGradient id="navGold" x1="0" x2="1">
        <stop offset="0" stop-color="#d6a73a"/><stop offset=".5" stop-color="#c9962f"/><stop offset="1" stop-color="#e0b03c"/>
      </linearGradient>
      <linearGradient id="navDark" x1="0" x2="1">
        <stop offset="0" stop-color="#2b2728"/><stop offset="1" stop-color="#55504f"/>
      </linearGradient>
    </defs>
    <polygon fill="url(#navGold)" points="100,0 452,0 464,32 112,32"/>
    <polygon fill="url(#navDark)" points="0,0 100,0 112,32 12,32"/>
  </svg>
  <div class="nav-items">
    <span style="left:43px">HOME</span>
    <span style="left:127px">ABOUT US</span>
    <span style="left:227px">OUR SERVICES</span>
    <span style="left:361px">NEWS</span>
  </div>
</nav>

<section class="abs welcome">
  <h2 class="welcome-title">WELCOME TO<b>Veralt</b></h2>
  <div class="welcome-rule"></div>
  <p class="welcome-copy">Lorem ipsum dolor sit amet, consectetur adipiscing elit, sed do eiusmod tempor incididunt ut labore et dolore magna aliqua.</p>
</section>

<section>
  <h2 class="abs news-title">NEWS</h2>
  <svg class="abs news-arrow" style="left:113px" viewBox="0 0 12 20"><polyline points="10,3 3,10 10,17" fill="none" stroke="#aaa" stroke-width="3"/></svg>
  <svg class="abs news-arrow" style="left:635px" viewBox="0 0 12 20"><polyline points="2,3 9,10 2,17" fill="none" stroke="#aaa" stroke-width="3"/></svg>
  <div class="abs news-rule"></div>

  <article class="abs post" style="left:113px">
    <div class="post-photo family" role="img" aria-label="Happy family lying together on a bed"></div>
    <p class="post-date">POSTED ON 04-07-2018</p>
    <p class="post-text">Lorem ipsum dolor sit amet, con-<br>sectetur adipiscing elit, sed do</p>
    <span class="post-btn">READ MORE</span>
  </article>
  <article class="abs post" style="left:301px">
    <div class="post-photo deal" role="img" aria-label="Handshake in front of a suburban house" style="width:165px;margin-top:-1px;height:110px"></div>
    <p class="post-date">POSTED ON 04-07-2018</p>
    <p class="post-text">Lorem ipsum dolor sit amet, con-<br>sectetur adipiscing elit, sed do</p>
    <span class="post-btn">READ MORE</span>
  </article>
  <article class="abs post" style="left:490px">
    <div class="post-photo family" role="img" aria-label="Happy family lying together on a bed"></div>
    <p class="post-date">POSTED ON 04-07-2018</p>
    <p class="post-text">Lorem ipsum dolor sit amet, con-<br>sectetur adipiscing elit, sed do</p>
    <span class="post-btn">READ MORE</span>
  </article>
</section>

<footer class="abs footer">
  <h3 class="abs foot-head" style="left:67px">QUICK LINKS</h3>
  <ul class="abs foot-list" style="left:67px">
    <li>Home</li><li>About Us</li><li>Services</li><li>News</li>
  </ul>
  <h3 class="abs foot-head" style="left:240px">CONTACT US</h3>
  <ul class="abs foot-list" style="left:240px">
    <li>Email: hello@veralt-mail.com</li>
    <li>Tel: (020) 4821 9036</li>
    <li>Street: Linden Row 14, Home Town</li>
  </ul>
  <h3 class="abs foot-head" style="left:516px">LOCATION MAP</h3>
  <div class="abs foot-map" role="img" aria-label="Street map showing the office location"></div>
  <div class="abs foot-rule"></div>
  <p class="abs foot-copy" style="left:15px">Copyright © 2018 Veralt Condo Services. All rights reserved</p>
  <p class="abs foot-copy" style="right:15px">Terms Of Service | Privacy Policy</p>
</footer>

</body>
</html>
```